Copperleaf Vantage Training PowerPoint Template

I want to PowerPoint template theme using my attached logo. My colors are black and orange. My website is CopperleafVantage.com. I am a handgun training company.

Font:

- Serpentine-Bold-Bold for "IRON BRAE"

- BrowalliaUPC for "SHOOTING SPORTS"

Colors (CMYK code):

- BLACK ....... 0; 0; 0; 100;
- ORANGE ... gradient from 0; 65; 97.5; 0 to 0; 39; 97.5; 0

```html
<!DOCTYPE html>
<html lang="en">
<head>
<meta charset="utf-8">
<title>Copperleaf Vantage Training – Presentation Template</title>
<link href="https://fonts.googleapis.com/css2?family=Russo+One&family=Arimo:wght@400;700&display=swap" rel="stylesheet">
<style>
  :root{
    --ink:#0b0d0e;
    --slate:#15191b;
    --slate-soft:#1d2225;
    --paper:#fafbfc;
    --orange-deep:#f45a06;
    --orange-warm:#f7a406;
    --orange-line:#f07c10;
    --muted:#8a8f93;
    --placeholder:#dfe1e2;
    --board-a:#3a3b3c;
    --board-b:#1b1c1d;
    --display:"Russo One", sans-serif;
    --body:"Arimo", Arial, sans-serif;
  }
  *{box-sizing:border-box;margin:0;padding:0}
  html,body{width:1200px;height:618px;overflow:hidden}
  body{
    position:relative;
    background:radial-gradient(ellipse at 75% 75%, var(--board-a), var(--board-b) 80%);
    font-family:var(--body);
  }
  .slide{position:absolute;width:385px;height:288px;overflow:hidden;background:var(--slate)}
  .slide--cover-a{left:12px;top:12px}
  .slide--cover-b{left:408px;top:12px}
  .slide--cover-c{left:805px;top:12px}
  .slide--list{left:12px;top:310px;background:var(--paper)}
  .slide--media{left:410px;top:310px;background:var(--paper)}

  .orange-fill{background:linear-gradient(90deg,var(--orange-deep),var(--orange-warm))}

  /* brand name block */
  .brand{position:absolute;display:flex;align-items:center;gap:9px;font-family:var(--display);color:var(--ink);text-transform:uppercase;line-height:1}
  .brand__mark{width:40px;height:40px;background:var(--orange-line);flex:none}
  .brand__name{font-size:19px;letter-spacing:.3px}
  .brand__name span{display:block}
  .brand--light{color:#fff}

  .title{font-family:var(--display);text-transform:uppercase;text-align:center;position:absolute;left:0;right:0}
  .subtext{position:absolute;left:0;right:0;text-align:center;color:#fff;font-size:9px;line-height:13.5px;text-transform:uppercase;letter-spacing:.2px}

  /* cover A */
  .cover-a__top{position:absolute;left:0;top:0;width:100%;height:155px;background:var(--paper)}
  .cover-a__band{position:absolute;left:0;top:155px;width:100%;height:25px}
  .cover-a__band .title{top:4px;font-size:17px;color:var(--ink)}
  .cover-a__band::after{content:"";position:absolute;left:0;bottom:-2px;width:100%;height:2px;background:#d9dcde}
  .slide--cover-a .brand{left:73px;top:96px}
  .slide--cover-a .subtext{top:194px;padding:0 90px}

  /* cover B */
  .slide--cover-b{background:linear-gradient(180deg,var(--ink) 0,var(--slate) 55%,var(--ink) 100%)}
  .cover-b__sheen{position:absolute;left:0;top:148px;width:100%;height:6px;background:linear-gradient(180deg,rgba(255,255,255,.08),transparent)}
  .slide--cover-b .brand{left:70px;top:108px}
  .slide--cover-b .title{top:178px;font-size:20px;color:#fff}
  .slide--cover-b .subtext{top:206px}
  .cover-b__bar{position:absolute;left:0;bottom:0;width:100%;height:24px}

  /* cover C */
  .cover-c__top{position:absolute;left:0;top:0;width:100%;height:148px;background:#fff}
  .cover-c__rule{position:absolute;left:0;top:148px;width:100%;height:5px;background:linear-gradient(180deg,var(--orange-line) 0 2px,#c9ced2 2px 3px,#2a3034 3px)}
  .slide--cover-c .brand{left:72px;top:104px}
  .slide--cover-c .title{top:194px;font-size:20px;color:var(--orange-warm)}
  .slide--cover-c .subtext{top:220px}

  /* content slides */
  .header{position:absolute;left:0;top:0;width:100%;height:40px;background:var(--ink);border-bottom:2px solid var(--orange-line)}
  .header h2{font-family:var(--display);font-weight:400;color:#fff;font-size:15px;text-transform:uppercase;position:absolute;left:12px;top:12px;letter-spacing:.3px}
  .footer{position:absolute;left:0;bottom:0;width:100%;height:29px;border-top:2px solid var(--ink)}
  .footer__copy{position:absolute;left:9px;top:9px;font-size:8.5px;color:var(--ink);text-transform:uppercase}
  .footer .brand{right:6px;top:2px}
  .footer .brand__mark{width:20px;height:20px}
  .footer .brand__name{font-size:10px}
  .footer .brand{gap:5px}

  .bullets{position:absolute;left:11px;top:56px;list-style:none}
  .bullets li{display:flex;align-items:center;gap:6px;height:24px;font-size:8.6px;font-weight:700;color:var(--ink)}
  .bullets svg{flex:none}

  .copy{position:absolute;left:17px;width:210px;font-size:8px;line-height:12.5px;color:var(--ink)}
  .copy--one{top:56px}
  .copy--two{top:152px}
  .img-slot{position:absolute;left:241px;width:133px;height:68px;background:var(--placeholder);display:flex;align-items:center;justify-content:center;font-size:8px;color:var(--muted)}
  .img-slot--one{top:84px}
  .img-slot--two{top:176px}
</style>
</head>
<body>

<section class="slide slide--cover-a">
  <div class="cover-a__top"></div>
  <div class="brand">
    <div class="brand__mark"></div>
    <div class="brand__name"><span>Copperleaf Vantage</span><span>Training</span></div>
  </div>
  <div class="cover-a__band orange-fill"><h1 class="title">Project Title Here</h1></div>
  <p class="subtext">Lorem ipsum dolor sit ipsum lorem ipsum dolor sit ipsum lorem ipsum dolor sit ipsum lorem ipsum dolor sit ipsum</p>
</section>

<section class="slide slide--cover-b">
  <div class="cover-b__sheen"></div>
  <div class="brand brand--light">
    <div class="brand__mark"></div>
    <div class="brand__name"><span>Copperleaf Vantage</span><span>Training</span></div>
  </div>
  <h1 class="title">Project Title Here</h1>
  <p class="subtext">Sub text here sub text here sub text here<br>sub text here sub text here</p>
  <div class="cover-b__bar orange-fill"></div>
</section>

<section class="slide slide--cover-c">
  <div class="cover-c__top"></div>
  <div class="cover-c__rule"></div>
  <div class="brand">
    <div class="brand__mark"></div>
    <div class="brand__name"><span>Copperleaf Vantage</span><span>Training</span></div>
  </div>
  <h1 class="title">Project Title Here</h1>
  <p class="subtext">Sub text here sub text here sub text here<br>sub text here sub text here</p>
</section>

<section class="slide slide--list">
  <header class="header"><h2>Project Title Here</h2></header>
  <ul class="bullets">
    <li><svg width="6" height="8" viewBox="0 0 6 8"><path d="M1 0.5 5 4 1 7.5" fill="none" stroke="#f07c10" stroke-width="1.8"/></svg>Lorem ipsum daolor sit ipsum Lorem ipsum dolor sit ipsum&nbsp; lorem ipsum</li>
    <li><svg width="6" height="8" viewBox="0 0 6 8"><path d="M1 0.5 5 4 1 7.5" fill="none" stroke="#f07c10" stroke-width="1.8"/></svg>Lorem ipsum daolor sit ipsum Lorem ipsum dolor sit ipsum&nbsp; lorem ipsum</li>
    <li><svg width="6" height="8" viewBox="0 0 6 8"><path d="M1 0.5 5 4 1 7.5" fill="none" stroke="#f07c10" stroke-width="1.8"/></svg>Lorem ipsum daolor sit ipsum Lorem ipsum dolor sit ipsum&nbsp; lorem ipsum</li>
    <li><svg width="6" height="8" viewBox="0 0 6 8"><path d="M1 0.5 5 4 1 7.5" fill="none" stroke="#f07c10" stroke-width="1.8"/></svg>Lorem ipsum daolor sit ipsum Lorem ipsum dolor sit ipsum&nbsp; lorem ipsum</li>
    <li><svg width="6" height="8" viewBox="0 0 6 8"><path d="M1 0.5 5 4 1 7.5" fill="none" stroke="#f07c10" stroke-width="1.8"/></svg>Lorem ipsum daolor sit ipsum Lorem ipsum dolor sit ipsum&nbsp; lorem ipsum</li>
    <li><svg width="6" height="8" viewBox="0 0 6 8"><path d="M1 0.5 5 4 1 7.5" fill="none" stroke="#f07c10" stroke-width="1.8"/></svg>Lorem ipsum daolor sit ipsum Lorem ipsum dolor sit ipsum&nbsp; lorem ipsum</li>
    <li><svg width="6" height="8" viewBox="0 0 6 8"><path d="M1 0.5 5 4 1 7.5" fill="none" stroke="#f07c10" stroke-width="1.8"/></svg>Lorem ipsum daolor sit ipsum Lorem ipsum dolor sit ipsum&nbsp; lorem ipsum</li>
    <li><svg width="6" height="8" viewBox="0 0 6 8"><path d="M1 0.5 5 4 1 7.5" fill="none" stroke="#f07c10" stroke-width="1.8"/></svg>Lorem ipsum daolor sit ipsum Lorem ipsum dolor sit ipsum&nbsp; lorem ipsum</li>
  </ul>
  <footer class="footer orange-fill">
    <span class="footer__copy">Copyright text here</span>
    <div class="brand">
      <div class="brand__mark"></div>
      <div class="brand__name"><span>Copperleaf Vantage</span><span>Training</span></div>
    </div>
  </footer>
</section>

<section class="slide slide--media">
  <header class="header"><h2>Project Title Here</h2></header>
  <p class="copy copy--one">Lorem ipsum daolor sit ipsum Lorem ipsum dolor sit ipsum Lorem ipsum dolor sit ipsum Lorem ipsum dolor sit ipsum Lorem ipsum daolor sit ipsum Lorem ipsum dolor sit ipsum Lorem ipsum dolor sit ipsum Lorem ipsum dolor sit ipsum Lorem ipsum daolor sit ipsum Lorem ipsum dolor sit ipsum Lorem ipsum dolor sit ipsum</p>
  <div class="img-slot img-slot--one">IMG HERE</div>
  <p class="copy copy--two">Lorem ipsum daolor sit ipsum Lorem ipsum dolor sit ipsum Lorem ipsum dolor sit ipsum Lorem ipsum dolor sit ipsum Lorem ipsum daolor sit ipsum Lorem ipsum dolor sit ipsum Lorem ipsum dolor sit ipsum Lorem ipsum dolor sit ipsum Lorem ipsum daolor sit ipsum Lorem ipsum dolor sit ipsum Lorem ipsum dolor sit ipsum</p>
  <div class="img-slot img-slot--two">IMG HERE</div>
  <footer class="footer orange-fill">
    <span class="footer__copy">Copyright text here</span>
    <div class="brand">
      <div class="brand__mark"></div>
      <div class="brand__name"><span>Copperleaf Vantage</span><span>Training</span></div>
    </div>
  </footer>
</section>

</body>
</html>
```